Ternhollow Partners

Need a new website - see more on ternhollowpartners.example

Target Market(s)

Finance industry = conservative design

Coding

Coded - Design and coding required

Number of Pages Required

5+ page

Requirements
Should not have
• Dear all,
• Please avoid pictures of people on the website (except the "team" of course :-)

```html
<!DOCTYPE html>
<html lang="en">
<head>
<meta charset="utf-8">
<title>Ternhollow Partners</title>
<link href="https://fonts.googleapis.com/css2?family=Roboto:wght@400;500&display=swap" rel="stylesheet">
<style>
  :root {
    --brand-red: #d0241b;
    --brand-red-dark: #b81d15;
    --ink: #2b2b2b;
    --ink-soft: #555555;
    --paper: #ffffff;
    --photo-haze: #b9c8d3;
    --photo-harbour: #7f9bb3;
    --photo-glass: #5d7588;
    --photo-deep: #34434f;
  }
  * { box-sizing: border-box; margin: 0; padding: 0; }
  html, body { width: 1200px; height: 676px; overflow: hidden; background: var(--paper); }
  body { font-family: "Roboto", Arial, sans-serif; color: var(--ink); position: relative; }
  a { text-decoration: none; }

  .site-header { position: relative; height: 106px; background: var(--paper); }
  .topbar {
    position: absolute; top: 0; right: 0; width: 790px; height: 42px;
    background: var(--brand-red);
    clip-path: polygon(0 0, 100% 0, 100% 100%, 42px 100%);
    display: flex; align-items: center; justify-content: flex-end;
    gap: 30px; padding-right: 40px; color: var(--paper); font-size: 13px;
  }
  .topbar-item { display: flex; align-items: center; gap: 6px; }
  .topbar svg { fill: var(--paper); }

  .brand { position: absolute; left: 50px; top: 22px; display: flex; align-items: center; gap: 10px; text-decoration: none; }
  .brand-dot { width: 62px; height: 62px; border-radius: 50%; background: var(--brand-red); flex: none; }
  .brand-name {
    color: var(--brand-red); font-size: 18px; font-weight: 400; line-height: 1.02;
    text-transform: uppercase; letter-spacing: 0.2px; text-decoration: none;
  }

  .main-nav { position: absolute; right: 44px; top: 60px; display: flex; gap: 38px; font-size: 13.5px; }
  .main-nav a { color: var(--ink); }
  .main-nav a.is-current { color: var(--brand-red); }

  .hero-photo {
    height: 390px;
    background: linear-gradient(100deg, var(--photo-haze) 0%, var(--photo-harbour) 28%, var(--photo-glass) 55%, var(--photo-harbour) 72%, var(--photo-deep) 100%);
  }

  .intro { text-align: center; padding-top: 24px; }
  .intro-title { font-size: 22px; font-weight: 400; line-height: 1.35; color: var(--ink); }
  .intro-lead { margin-top: 12px; font-size: 13px; color: var(--ink-soft); }
  .cta {
    display: inline-flex; align-items: center; gap: 10px; margin-top: 22px;
    padding: 10px 20px; border: 1.5px solid var(--brand-red); border-radius: 24px;
    color: var(--brand-red-dark); font-size: 14px; font-weight: 500;
  }
  .cta svg { fill: var(--brand-red); }
</style>
</head>
<body>
  <header class="site-header">
    <div class="topbar">
      <span class="topbar-item">
        <svg width="12" height="12" viewBox="0 0 24 24"><path d="M6.6 10.8a15.1 15.1 0 0 0 6.6 6.6l2.2-2.2c.3-.3.7-.4 1-.2 1.1.4 2.3.6 3.6.6.6 0 1 .4 1 1V20c0 .6-.4 1-1 1A17 17 0 0 1 3 4c0-.6.4-1 1-1h3.5c.6 0 1 .4 1 1 0 1.3.2 2.5.6 3.6.1.3 0 .7-.2 1z"/></svg>
        +1 800 555 01 47
      </span>
      <span class="topbar-item">
        <svg width="13" height="10" viewBox="0 0 26 20"><path d="M0 0h26v20H0zM2 3v1l11 7 11-7V3L13 10z"/></svg>
        info@ternhollowpartners.example
      </span>
      <svg width="13" height="13" viewBox="0 0 24 24"><path d="M10 2a8 8 0 0 1 6.3 12.9l5.4 5.4-2 2-5.4-5.4A8 8 0 1 1 10 2zm0 3a5 5 0 1 0 0 10 5 5 0 0 0 0-10z"/></svg>
    </div>

    <a class="brand" href="#">
      <span class="brand-dot"></span>
      <span class="brand-name">Ternhollow<br>Partners</span>
    </a>

    <nav class="main-nav">
      <a class="is-current" href="#">HOME</a>
      <a href="#">SERVICES</a>
      <a href="#">CURRENT ENGAGEMENTS</a>
      <a href="#">NEWS</a>
      <a href="#">TEAM</a>
      <a href="#">CONTACT US</a>
    </nav>
  </header>

  <div class="hero-photo" role="img" aria-label="Office interior with tall windows overlooking a harbour with ships and cranes"></div>

  <section class="intro">
    <h1 class="intro-title">Founded in 2004, Ternhollow is headquartered in Gibraltar<br>with representative offices in Luxembourg and London</h1>
    <p class="intro-lead">See some of the features below and learn why businesses trust Ternhollow</p>
    <a class="cta" href="#">
      <svg width="10" height="11" viewBox="0 0 10 11"><path d="M0 0l10 5.5L0 11z"/></svg>
      Learn about Ternhollow
    </a>
  </section>
</body>
</html>
```